Covid 19 Exit Strategy one page brochure

I would like to design, and will need URGENT help, a brochure detailing a Covid 19 Exit Strategy plan. This brochure will need to be understood easily and the graphics inside should make it easy for people to understand without reading the entire text. This project is quite urgent and needs to be completed THIS WEEK - by Saturday may 16th at the latest. I am attaching two examples. I will provide the text.

```html
<!DOCTYPE html>
<html lang="en">
<head>
<meta charset="utf-8">
<title>COVID-19 Phased Exit Strategy</title>
<link rel="stylesheet" href="https://fonts.googleapis.com/css2?family=Roboto+Condensed:wght@700&family=PT+Sans:wght@400;700&family=Roboto:wght@700;900&display=swap">
<style>
:root{
  --stage-bg:#3b3c3e;
  --paper:#ffffff;
  --paper-tint:#eef0f3;
  --blue:#1f6aa5;
  --blue-deep:#17558a;
  --ink:#2b2c2e;
  --ink-soft:#3a3a3a;
  --charcoal:#2f3033;
  --rule:#5a5a5a;
}
*{box-sizing:border-box;margin:0;padding:0}
html,body{width:1200px;height:900px;overflow:hidden}
body{background:var(--stage-bg);font-family:"PT Sans",Arial,sans-serif;color:var(--ink-soft)}
.brochure{
  position:absolute;left:305px;top:10px;width:590px;height:880px;
  background:linear-gradient(180deg,var(--paper) 0%,var(--paper-tint) 45%,#f6f7f9 100%);
  overflow:hidden;
}
.hero-texture{position:absolute;left:0;top:0;width:590px;height:300px;
  background:radial-gradient(ellipse at 30% 30%,#c9d2dc 0%,rgba(220,226,233,.6) 45%,rgba(255,255,255,0) 75%)}
.lower-texture{position:absolute;left:0;top:560px;width:590px;height:240px;
  background:linear-gradient(160deg,rgba(255,255,255,0) 30%,#dfe3e8 60%,rgba(255,255,255,0) 90%)}
.band{position:absolute;left:0;top:0}
.title-badge{position:absolute;left:0;top:0}
.badge-text{position:absolute;left:44px;top:130px;width:200px;text-align:center;color:var(--ink)}
.badge-title{font-family:"Roboto",Arial,sans-serif;font-weight:900;font-size:33px;letter-spacing:-.5px;line-height:1}
.badge-sub{font-family:"Roboto",Arial,sans-serif;font-weight:700;font-size:15px;margin-top:4px}
.author{position:absolute;left:266px;top:52px;width:310px;text-align:center;font-family:"Roboto Condensed",Arial,sans-serif;font-weight:700;line-height:1}
.author-label{font-size:26px;color:var(--ink);letter-spacing:.5px}
.author-name{font-size:40px;color:var(--blue);margin-top:2px;letter-spacing:.5px}
.dotted-rule{position:absolute;left:266px;top:133px;width:312px;border-top:2px dotted var(--ink)}
.intro{position:absolute;left:266px;top:143px;width:314px;font-size:8.6px;line-height:1.3;text-align:justify}
.section-bar{position:absolute;display:flex;align-items:center;justify-content:center;
  font-family:"Roboto Condensed",Arial,sans-serif;font-weight:700;color:#fff;letter-spacing:.5px}
.bar-general{left:186px;top:268px;width:336px;height:26px;font-size:18px;
  background:linear-gradient(90deg,rgba(47,48,51,0) 0%,var(--charcoal) 12%,var(--charcoal) 78%,rgba(47,48,51,0) 100%)}
.bar-plan{left:48px;top:452px;width:510px;height:28px;font-size:18px;
  background:linear-gradient(90deg,rgba(31,106,165,0) 0%,var(--blue) 14%,var(--blue) 80%,rgba(31,106,165,0) 100%)}
.requirements{position:absolute;top:306px;font-size:8.6px;line-height:1.3}
.req-left{left:30px;width:280px}
.req-right{left:338px;width:248px;text-align:justify}
.stages-tab{position:absolute;left:14px;top:522px;width:30px;height:272px;background:var(--charcoal);
  display:flex;align-items:center;justify-content:center}
.stages-tab span{transform:rotate(-90deg);white-space:nowrap;color:#fff;font-family:"Roboto Condensed",Arial,sans-serif;
  font-weight:700;font-size:17px;letter-spacing:9px}
.stage-tree{position:absolute;left:0;top:0}
.stage{position:absolute;left:100px;width:484px}
.stage-lead{font-size:8.4px;font-weight:700;line-height:1.3;color:var(--ink)}
.stage-cols{display:flex;margin-top:8px}
.stage-cols p{font-size:8.4px;line-height:1.3;padding:0 6px;text-align:justify;flex:1}
.stage-cols p:first-child{padding-left:0}
.stage-cols p+p{border-left:1px solid var(--rule)}
.stage-1{top:498px}
.stage-2{top:588px}
.stage-3{top:704px}
.footer{position:absolute;left:0;top:808px;width:590px;height:50px;display:flex}
.footer-cta{width:282px;background:var(--blue);color:#fff;display:flex;align-items:center;justify-content:center;
  font-family:"Roboto Condensed",Arial,sans-serif;font-weight:700;font-size:19px;letter-spacing:.5px}
.footer-motto{flex:1;background:var(--charcoal);color:#fff;display:flex;align-items:center;justify-content:center;gap:10px;
  font-family:"Roboto",Arial,sans-serif;font-weight:700;font-size:16px;letter-spacing:.5px}
</style>
</head>
<body>
<main class="brochure">
  <div class="hero-texture" role="img" aria-label="Faint background image of virus particles"></div>
  <div class="lower-texture" role="img" aria-label="Soft grey geometric background shapes"></div>

  <svg class="band" width="590" height="300" viewBox="0 0 590 300" aria-hidden="true">
    <polygon points="138,0 384,0 0,270 0,97" fill="#1f6aa5"/>
    <polygon points="0,97 138,0 60,0 0,42" fill="#cfd6de" opacity=".7"/>
  </svg>

  <svg class="title-badge" width="300" height="300" viewBox="0 0 300 300" aria-hidden="true">
    <circle cx="144" cy="168" r="100" fill="#fff"/>
    <circle cx="144" cy="168" r="96" fill="none" stroke="#2b2c2e" stroke-width="3"/>
    <path d="M 240 168 A 96 96 0 0 1 144 264" fill="none" stroke="#1f6aa5" stroke-width="5"/>
  </svg>
  <div class="badge-text">
    <div class="badge-title">COVID-19</div>
    <div class="badge-sub">Phased Exit Strategy</div>
  </div>

  <header class="author">
    <div class="author-label">DEVELOPED BY</div>
    <div class="author-name">LINA HADDAD</div>
  </header>
  <div class="dotted-rule"></div>

  <p class="intro">Pandemics have, historically, seen their end both medically - via herd immunity or immunizations. And while there are several clinical trials underway for potential Covid-19 vaccines, we are still a long way from deploying an effective vaccine and one that will stand the test of time as the virus changes. Covid-19 pandemic will be considered 'ended' when there are only occasional traces of localized cases that are quickly contained in specific locations. Today and in the absence of an effective vaccine(s) and for the re-opening of the economies and social activities to be successful, it is critical that the following basic conditions be in place before any lockdowns are lifted and before social activities resume:</p>

  <h2 class="section-bar bar-general">GENERAL REQUIREMENTS</h2>

  <div class="requirements req-left">
    <p>Single digit downward trend of documented cases within the past 14-days.</p>
    <p>Hospitals and the health care system are capable of treating patients without operating on a crisis mode.</p>
    <p>Ability to screen and test symptomatic individuals within 24 hours of identification. Increased and sufficient testing capacity, to test at least 50% of all population if necessary within a timeframe of 3 months.</p>
    <p>Ability to surge ICU capacity on a short notice - 24h.</p>
    <p>Ability to track and trace infected patients and contacts on a live basis and across the country and ability to react quickly to any unusual trends or outbreaks.</p>
  </div>
  <div class="requirements req-right">
    <p>Plan in place to trigger targeted or full-scale containment in case of sudden outbreaks</p>
    <p>Mandatory use of masks (at least surgical grade) for everyone in all public areas and at work. Mandatory use of N95, or equivalent, masks for all healthcare front workers and for all government agencies and authorities that are involved in overseeing the containment activities.</p>
    <p>Mandatory daily checks of body temperature for everyone at the workplace or entering public areas.</p>
    <p>Mandatory sanitation in all places - use of disinfection available on a large scale</p>
  </div>

  <h2 class="section-bar bar-plan">PHASED COVID-19 LOCKDOWN EXIT STRATEGY PLAN</h2>

  <div class="stages-tab"><span>STAGES</span></div>
  <svg class="stage-tree" width="100" height="880" viewBox="0 0 100 880" aria-hidden="true">
    <path d="M44 658 H56 M76 528 H62 V792 H44 M62 622 H76 M62 739 H76" fill="none" stroke="#1f6aa5" stroke-width="2.5"/>
    <path d="M76 516 H100 M76 610 H100 M76 727 H100" fill="none" stroke="#1f6aa5" stroke-width="1.5"/>
    <g font-family="Roboto Condensed, Arial, sans-serif" font-weight="700" font-size="15" text-anchor="middle">
      <circle cx="76" cy="516" r="12" fill="#fff" stroke="#1f6aa5" stroke-width="3"/>
      <text x="76" y="521.5" fill="#2b2c2e">1</text>
      <circle cx="76" cy="610" r="12" fill="#fff" stroke="#1f6aa5" stroke-width="3"/>
      <text x="76" y="615.5" fill="#2b2c2e">2</text>
      <circle cx="76" cy="727" r="12" fill="#fff" stroke="#1f6aa5" stroke-width="3"/>
      <text x="76" y="732.5" fill="#2b2c2e">3</text>
    </g>
  </svg>

  <section class="stage stage-1">
    <p class="stage-lead">To enter this stage, additional to the general requirements, the Effective Reproduction Number (Rt) must be less than 1 and the death rate at less than 3%.</p>
    <div class="stage-cols">
      <p>Elderly (60+ years old) and vulnerable individuals should continue to self-isolate.</p>
      <p>No more than 5 people maximum gathering at a time in public areas and at work.</p>
      <p>Work from home should continue whenever and as much as possible.</p>
    </div>
  </section>

  <section class="stage stage-2">
    <p class="stage-lead">To enter stage 2 of the Covid-19 Exit Strategy, compliance to the general requirements is compulsory, additional to a successful Stage 1 outcome. The Effective Reproduction Number (Rt) for Stage 2 must be less than 0.5 and the death rate stabilized at less than 1.5%.</p>
    <div class="stage-cols">
      <p>Elderly (60+ years old) and vulnerable individuals should continue to self-isolate as much as possible.</p>
      <p>No more than 10 people maximum gathering at a time in public areas and at work.</p>
      <p>Work from home should if possible or for jobs that do not have to be necessarily in an office setup.</p>
    </div>
  </section>

  <section class="stage stage-3">
    <p class="stage-lead">To enter stage 3 of the Covid-19 Exit Strategy, compliance to the general requirements is compulsory, additional to a successful Stage 2 outcome. The Effective Reproduction Number (Rt) for Stage 3 must be less than 0.3 and the death rate stabilized at less than 1%</p>
    <div class="stage-cols">
      <p>Elderly (60+ years old) and vulnerable individuals may resume all previously exercised activities without restrictions.</p>
      <p>Restrictions as to the number of people gathering together can be lifted. Social distancing can be relaxed. However, wear of masks may continue</p>
      <p>Religious sites can operate normally. Wear of masks should be elective.</p>
    </div>
  </section>

  <footer class="footer">
    <div class="footer-cta">LETS STOP COVID-19</div>
    <div class="footer-motto">
      <span>STAY</span>
      <svg width="36" height="32" viewBox="0 0 36 32" aria-label="Home icon" role="img">
        <path d="M18 2 L2 16 H7 V30 H15 V21 H21 V30 H29 V16 H34 Z" fill="#fff"/>
      </svg>
      <span>STAY SAFE</span>
    </div>
  </footer>
</main>
</body>
</html>
```